Accommodation business card design

We need a business card designed for our long-term accommodation business based in Australia. The business card must match the style of the attached letterhead and logo. The same contact details that are on the letterhead will also go on the card except that the card must list the contact details in the following order:phone, email, home address, ABN.

The card will be printed on .76mm white pvc plastic (same as credit cards), printed both sides and will be silver foil stamped on at least one side (preferably 2 sides) The design template is attached, but please go to www.zt.com.au for more specs.

The only other addition the card will be my name: Malcolm Darby

```html
<!DOCTYPE html>
<html lang="en">
<head>
<meta charset="utf-8">
<title>Summit Stays Accommodation – Business Card</title>
<link rel="stylesheet" href="https://fonts.googleapis.com/css2?family=Carlito:wght@400;700&display=swap">
<style>
  :root {
    --paper: #ffffff;
    --logo-grey: #bcbdbf;
    --text-grey: #585a5d;
    --text-dark: #2f3033;
    --maroon: #6e2136;
    --brick: #894b42;
    --swoosh-grey: #bbbcbe;
    --rule: #1a1a1a;
  }
  * { box-sizing: border-box; margin: 0; padding: 0; }
  html, body { width: 1003px; height: 1200px; overflow: hidden; background: var(--paper); }
  body { font-family: "Carlito", "Calibri", sans-serif; }

  .card { position: relative; width: 1003px; height: 1200px; background: var(--paper); overflow: hidden; }

  /* Front: brand */
  .card-front { position: absolute; left: 0; top: 0; width: 1003px; height: 594px; border-bottom: 1px solid var(--rule); }
  .brand-mark { position: absolute; left: 80px; top: 168px; width: 248px; height: 260px; border-radius: 26px; background: var(--logo-grey); }
  .brand-name {
    position: absolute; left: 372px; top: 186px; width: 560px;
    color: var(--logo-grey); font-weight: 700; text-transform: uppercase; line-height: 0.95;
  }
  .brand-name .line-main { display: block; font-size: 128px; letter-spacing: 2px; }
  .brand-name .line-sub { display: block; font-size: 67px; letter-spacing: 0px; margin-top: 6px; }

  /* Back: contact details */
  .contact-list { position: absolute; left: 54px; top: 608px; list-style: none; }
  .contact-item { display: flex; align-items: center; height: 51px; font-size: 32px; color: var(--text-grey); }
  .contact-item .icon { width: 34px; height: 34px; margin-right: 15px; flex: none; }
  .contact-item.indent { padding-left: 49px; }
  .contact-item.address { color: var(--text-dark); }
  .abn-label { color: var(--maroon); margin-right: 8px; }

  .footer-band { position: absolute; left: 0; top: 0; width: 1003px; height: 1200px; }

  .holder { position: absolute; right: 48px; top: 1048px; text-align: right; color: var(--paper); }
  .holder-name { font-size: 64px; line-height: 1; letter-spacing: 1px; }
  .holder-role { font-size: 36px; letter-spacing: 8px; margin-top: 6px; line-height: 1; }
</style>
</head>
<body>
<main class="card">
  <section class="card-front">
    <div class="brand-mark" aria-hidden="true"></div>
    <h1 class="brand-name">
      <span class="line-main">Summit</span>
      <span class="line-sub">Accommodation</span>
    </h1>
  </section>

  <svg class="footer-band" viewBox="0 0 1003 1200" aria-hidden="true">
    <path fill="var(--swoosh-grey)" d="M254 947 C 520 995 800 960 1003 877 L1003 958 C 790 1010 500 1000 254 947 Z"/>
    <path fill="var(--brick)" d="M0 891 C 300 985 650 1030 1003 978 L1003 1200 L0 1200 Z"/>
  </svg>

  <ul class="contact-list">
    <li class="contact-item">
      <svg class="icon" viewBox="0 0 34 34" aria-hidden="true">
        <circle cx="17" cy="17" r="17" fill="var(--maroon)"/>
        <path fill="#fff" d="M11 9 l4 -1 2 6 -3 2 c1 3 3 5 6 6 l2 -3 6 2 -1 4 c-1 2 -3 2 -5 2 c-7 -2 -12 -7 -13 -14 c0 -2 1 -4 2 -4 z"/>
      </svg>
      0400 318 562
    </li>
    <li class="contact-item">
      <svg class="icon" viewBox="0 0 34 34" aria-hidden="true">
        <circle cx="17" cy="17" r="17" fill="var(--maroon)"/>
        <rect x="8" y="11" width="18" height="13" rx="1.5" fill="none" stroke="#fff" stroke-width="2"/>
        <path d="M8.5 12 L17 19 L25.5 12" fill="none" stroke="#fff" stroke-width="2"/>
      </svg>
      malcolm.darby@mailbox.com.au
    </li>
    <li class="contact-item address">
      <svg class="icon" viewBox="0 0 34 34" aria-hidden="true">
        <circle cx="17" cy="17" r="17" fill="var(--maroon)"/>
        <path d="M7 17 L17 8 L27 17" fill="none" stroke="#fff" stroke-width="2.4" stroke-linejoin="round"/>
        <path d="M11 16 V26 H23 V16" fill="none" stroke="#fff" stroke-width="2.2"/>
        <rect x="15" y="19" width="4" height="7" fill="#fff"/>
      </svg>
      PO Box 7318, Harbourside Mail Centre
    </li>
    <li class="contact-item indent address">QLD 4700</li>
    <li class="contact-item indent"><span class="abn-label">ABN</span>51 208 774 903</li>
  </ul>

  <div class="holder">
    <p class="holder-name">MALCOLM DARBY</p>
    <p class="holder-role">POSITION</p>
  </div>
</main>
</body>
</html>
```